Hairdressing Salon called; Velvet Tress. Style Lives Here

Velvet Tress
We Love Hair
418 Penrose Lane Birch Vale
5183742
Business card not to fussy.
I would like it to be a Black background with White and/or Grey lettering.

I really like the business card attached, so if the front looked like this I would be really happy, but would also like my address and phone number on the front.

On the back I would like two options of
1: reward card; buy any Haircare product over $20 on any visit and on the tenth product receive a complimentry Treatment and
2: appointment times and date

Industry/Entity Type

Business

Contact Information for Business Card

Velvet Tress
We Love Hair
5183742
418 Penrose Lane, Birch Vale
This must all be included on the front of the card

Font styles to use
Serif
Decorative
Script

Colors
1b1b1b
757575
ffffff

Requirements
Must have
• My phone number and address
Should not have
• Pictures on the front

```html
<!DOCTYPE html>
<html lang="en">
<head>
<meta charset="utf-8">
<title>Velvet Tress – Reward Card</title>
<link href="https://fonts.googleapis.com/css2?family=Tinos&family=Pinyon+Script&display=swap" rel="stylesheet">
<style>
  :root {
    --card-black: #000000;
    --rule-grey: #757575;
    --text-grey: #6e6e6e;
    --ornament-grey: #3c3d3e;
  }
  html, body {
    margin: 0;
    padding: 0;
    width: 1200px;
    height: 857px;
    overflow: hidden;
    background: var(--card-black);
  }
  .card-back {
    position: relative;
    width: 1200px;
    height: 857px;
    background: var(--card-black);
    overflow: hidden;
  }
  .edge-rule {
    position: absolute;
    top: 0;
    width: 1px;
    height: 100%;
    background: var(--rule-grey);
    opacity: 0.7;
  }
  .edge-rule--outer { left: 86px; }
  .edge-rule--inner { left: 129px; }
  .flourish {
    position: absolute;
  }
  .flourish--top {
    left: 880px;
    top: 0;
    width: 320px;
    height: 196px;
    background: radial-gradient(ellipse at 60% 40%, rgba(60,61,62,0.75) 0%, rgba(60,61,62,0.35) 45%, rgba(0,0,0,0) 72%);
  }
  .flourish--bottom {
    left: 503px;
    top: 330px;
    width: 652px;
    height: 527px;
    background: radial-gradient(ellipse at 55% 65%, rgba(60,61,62,0.85) 0%, rgba(60,61,62,0.45) 45%, rgba(0,0,0,0) 72%);
  }
  .reward-copy {
    position: absolute;
    left: 194px;
    top: 182px;
    margin: 0;
    font-family: "Tinos", "Times New Roman", serif;
    font-size: 39px;
    line-height: 51px;
    color: var(--text-grey);
    white-space: nowrap;
  }
  .reward-title .initial {
    font-family: "Pinyon Script", cursive;
    font-size: 46px;
    letter-spacing: -2px;
  }
</style>
</head>
<body>
  <main class="card-back">
    <div class="edge-rule edge-rule--outer"></div>
    <div class="edge-rule edge-rule--inner"></div>

    <div class="flourish flourish--top" role="img" aria-label="Grey swirling floral flourish in the top right corner"></div>
    <div class="flourish flourish--bottom" role="img" aria-label="Grey swirling floral vine ornament rising from the bottom edge"></div>

    <p class="reward-copy">
      <span class="reward-title"><span class="initial">R</span>eward card;</span><br>
      buy any Haircare product over $20 on any<br>
      visit and on the tenth product receive a<br>
      complimentry Treatment and<br>
      appointment times and date
    </p>
  </main>
</body>
</html>
```